Mailchimp Email Design for Weekly New Products Email

We would like to send a weekly email to our customers highlighting four of the new jewelry pieces we have for sale each week. The email should be professionally looking, and have the same look and feel of our website, calderwinnjewelers.com. The template would have our logo on the top or left header, and would then have a block of text which would stay the same each week. This block would say "This weeks new arrivals won't last long, shop now with discount code "EMAIL10" to receive 10% off your entire purchase!"
Then below that, there would space for four images, which I will need to change every week. Below each image, there should be room for a title description of the image, which I will need to change each week. An example title would be "18k Yellow Gold Curb Necklace"
Then below the found images, maybe a black action button that says "SHOP NOW". Also, each of the images should be clickable links, which I can edit to add the link to the specific item.
I have attached a few images so you can use them for the mockup. Also, if there are any other ideas you have to make it look better please do!
Thanks,
Tad
It only allowed me to upload one image, so I uploaded the EPS file of our logo. You can use the product images from our website, calderwinnjewelers.com for the product images for now.

```html
<!DOCTYPE html>
<html lang="en">
<head>
<meta charset="utf-8">
<title>Calder Winn Jewelers – Weekly New Arrivals</title>
<link rel="stylesheet" href="https://fonts.googleapis.com/css2?family=Arimo:wght@400;700&display=swap">
<style>
  :root {
    --page-bg: #f9f9f9;
    --page-band: #fbf6f5;
    --email-bg: #f2f2f2;
    --header-bg: #ffffff;
    --ink: #222222;
    --ink-soft: #333333;
    --accent: #e0a526;
    --rule: #8a8a8a;
    --divider: #e2e2e2;
    --button-bg: #000000;
    --button-ink: #ffffff;
    --footer-bg: #222222;
    --footer-ink: #ffffff;
    --card-border: #d9d9d9;
  }
  * { box-sizing: border-box; margin: 0; padding: 0; }
  html, body { width: 939px; height: 1200px; overflow: hidden; }
  body {
    background: linear-gradient(var(--page-band) 0 55px, var(--page-bg) 55px);
    font-family: "Arimo", Arial, sans-serif;
    color: var(--ink);
  }
  .email {
    width: 560px; height: 1200px; margin: 0 auto;
    background: var(--email-bg);
    display: flex; flex-direction: column;
  }
  .brand-header {
    height: 55px; background: var(--header-bg);
    display: flex; align-items: center; justify-content: center;
  }
  .brand-name {
    font-family: "Arimo", Arial, sans-serif;
    font-weight: 400; font-size: 18px; color: var(--ink); line-height: 1;
  }
  .hero {
    height: 273px;
    background:
      linear-gradient(#000 0 10px, transparent 10px),
      radial-gradient(ellipse at 55% 45%, #8f877a 0%, #4b4a4c 35%, #23262d 75%);
  }
  .offer {
    margin: 0 17px; height: 89px; border-bottom: 1px solid var(--rule);
    text-align: center; padding-top: 6px;
  }
  .offer-lead { font-size: 23px; line-height: 26px; color: var(--ink); }
  .offer-code { font-size: 17px; line-height: 22px; color: var(--ink-soft); }
  .offer-close { font-size: 23px; line-height: 28px; color: var(--ink); }
  .accent { color: var(--accent); }
  .product-row {
    margin: 0 17px; padding: 26px 0 22px;
    display: flex; gap: 30px;
    border-bottom: 1px solid var(--divider);
  }
  .product {
    width: 248px; text-align: center; text-decoration: none; color: var(--ink);
    display: flex; flex-direction: column; align-items: center;
  }
  .product-photo { width: 248px; height: 196px; border: 1px solid var(--card-border); }
  .photo-gold-necklace { background: radial-gradient(ellipse at 50% 35%, #ffffff 0%, #f1f0ee 45%, #d9b45a 70%, #ece9e4 85%); }
  .photo-lapis-cufflinks { background: radial-gradient(ellipse at 50% 50%, #3346b8 0%, #5b6cc4 18%, #e7edf3 40%, #f1f4f7 100%); }
  .photo-onyx-ring { background: radial-gradient(ellipse at 48% 47%, #2a2a35 0%, #c9b58a 22%, #ffffff 42%); }
  .photo-braided-chain { background: radial-gradient(ellipse at 50% 38%, #ffffff 0%, #f2f1ef 42%, #c79a4e 66%, #f1efeb 84%); }
  .product-title {
    margin-top: 16px; font-size: 13px; letter-spacing: -0.2px;
    line-height: 19px; height: 38px; width: 252px; white-space: nowrap;
  }
  .shop-button {
    margin-top: 18px; background: var(--button-bg); color: var(--button-ink);
    font-size: 13.5px; line-height: 15px; padding: 0 4px;
  }
  .footer {
    margin-top: auto; height: 103px; background: var(--footer-bg); color: var(--footer-ink);
    display: flex; flex-direction: column; align-items: center; padding-top: 20px;
  }
  .social-links { display: flex; gap: 26px; }
  .social-links svg { width: 24px; height: 24px; display: block; }
  .copyright { margin-top: 23px; font-size: 11px; }
  .copyright a { color: var(--footer-ink); }
</style>
</head>
<body>
  <main class="email">
    <header class="brand-header">
      <div class="brand-name">Calder Winn Jewelers</div>
    </header>

    <div class="hero" role="img" aria-label="Assorted vintage silver and gold jewelry — watch, chains, bracelet and rings — on a dark background"></div>

    <section class="offer">
      <p class="offer-lead">This week's new arrivals won't last long,</p>
      <p class="offer-code">shop now with discount code &nbsp;<span class="accent">"EMAIL10"</span>&nbsp; to</p>
      <p class="offer-close">receive <span class="accent">10% off</span> your entire purchase!</p>
    </section>

    <section class="product-row">
      <a class="product" href="#">
        <div class="product-photo photo-gold-necklace" role="img" aria-label="Yellow gold mesh wheat necklace on a white display bust"></div>
        <p class="product-title">18k Yellow Gold Diamond Emerald Fancy<br>Mesh Wheat Necklace 17.5"</p>
        <span class="shop-button">SHOP NOW</span>
      </a>
      <a class="product" href="#">
        <div class="product-photo photo-lapis-cufflinks" role="img" aria-label="Pair of oval blue lapis stones set in gold"></div>
        <p class="product-title">18k Yellow Gold Diamond Emerald Fancy<br>Mesh Wheat Necklace 17.5"</p>
        <span class="shop-button">SHOP NOW</span>
      </a>
    </section>

    <section class="product-row">
      <a class="product" href="#">
        <div class="product-photo photo-onyx-ring" role="img" aria-label="Gold ring with black onyx and mother of pearl inlay"></div>
        <p class="product-title">14k Yellow Gold Black Onyx and Mother of<br>Pearl Inlay Ring Size 7</p>
        <span class="shop-button">SHOP NOW</span>
      </a>
      <a class="product" href="#">
        <div class="product-photo photo-braided-chain" role="img" aria-label="Braided yellow gold wheat chain necklace on a white display bust"></div>
        <p class="product-title">14k Yellow Gold 35.2g Soft Braided Wheat<br>Chain Necklace Italy 17 Inches</p>
        <span class="shop-button">SHOP NOW</span>
      </a>
    </section>

    <footer class="footer">
      <nav class="social-links" aria-label="Social links">
        <a href="#" aria-label="Photo feed">
          <svg viewBox="0 0 24 24"><circle cx="12" cy="12" r="10.5" fill="none" stroke="#fff" stroke-width="1.5"/></svg>
        </a>
        <a href="#" aria-label="Website">
          <svg viewBox="0 0 24 24" fill="none" stroke="#fff" stroke-width="1.5" stroke-linecap="round">
            <circle cx="12" cy="12" r="10.5"/>
            <path d="M11 9.5l1.3-1.3a2 2 0 0 1 2.9 2.9L13.9 12.4M13 14.5l-1.3 1.3a2 2 0 0 1-2.9-2.9l1.3-1.3M10.5 13.5l3-3"/>
          </svg>
        </a>
        <a href="#" aria-label="Pin board">
          <svg viewBox="0 0 24 24"><circle cx="12" cy="12" r="10.5" fill="none" stroke="#fff" stroke-width="1.5"/></svg>
        </a>
      </nav>
      <p class="copyright">© 2020 <a href="#">Calder Winn Jewelers</a></p>
    </footer>
  </main>
</body>
</html>
```